No Credit Score QT and ZMR

I'm looking for a banner to display on emails as well as facebook. The facebook banner would need to be square and the other size is 728 x 90. We are a mortgage company that does mostly Military home loans. We would like to start out with just this banner, then do about 20 others once we find the right designer. I need something simple but that stands out. Our company website is www.harborpeakfinancial.com. The text for this will be ( Ask about our "No Credit Score" program for ZMR and QT)

```html
<!DOCTYPE html>
<html lang="en">
<head>
<meta charset="utf-8">
<title>No Credit Score Banner 728 x 90</title>
<link rel="stylesheet" href="https://fonts.googleapis.com/css2?family=Bebas+Neue&family=Open+Sans:wght@400&display=swap">
<style>
  :root {
    --stage: #e8e9ea;
    --label: #9a9a9a;
    --panel: #58585a;
    --panel-edge: #6a6a6c;
    --green: #7aa23d;
    --white: #ffffff;
    --photo-top: #b7a597;
    --photo-bottom: #6d7a52;
    --emblem: #ececec;
  }
  * { margin: 0; padding: 0; box-sizing: border-box; }
  html, body { width: 1200px; height: 379px; overflow: hidden; background: var(--stage); }
  .stage { position: relative; width: 1200px; height: 379px; }
  .size-label {
    position: absolute; left: 109px; top: 102px;
    font-family: "Bebas Neue", sans-serif; font-size: 15px; letter-spacing: 1px;
    color: var(--label);
  }
  .banner {
    position: absolute; left: 108px; top: 131px; width: 1002px; height: 125px;
    background: var(--panel);
    box-shadow: 2px 4px 5px rgba(0,0,0,0.35);
    overflow: hidden;
  }
  .banner-shapes { position: absolute; inset: 0; }
  .emblem {
    position: absolute; left: 314px; top: 9px; width: 74px; height: 106px;
  }
  .offer {
    position: absolute; left: 400px; top: 0; width: 290px; height: 125px;
    display: flex; flex-direction: column; align-items: center; justify-content: center;
    font-family: "Bebas Neue", sans-serif; color: var(--white); text-align: center;
    line-height: 1;
  }
  .offer-line { font-size: 25px; letter-spacing: 0.3px; }
  .offer-highlight { font-size: 34px; color: var(--green); margin: 3px 0 4px; letter-spacing: 0.3px; }
  .cta {
    position: absolute; left: 704px; top: 0; width: 298px; height: 125px;
    border-left: 1px solid var(--panel-edge);
  }
  .cta-button {
    position: absolute; left: 12px; top: 32px; width: 204px; height: 46px;
    background: var(--green); color: var(--white);
    font-family: "Bebas Neue", sans-serif; font-size: 23px; letter-spacing: 1px;
    display: flex; align-items: center; justify-content: center;
    box-shadow: 2px 3px 4px rgba(0,0,0,0.35);
  }
  .cta-url {
    position: absolute; left: 0; top: 90px; width: 228px; text-align: center;
    font-family: "Open Sans", sans-serif; font-size: 14px; color: var(--white);
  }
</style>
</head>
<body>
<div class="stage">
  <div class="size-label">728 X 90</div>
  <div class="banner">
    <svg class="banner-shapes" width="1002" height="125" viewBox="0 0 1002 125">
      <defs>
        <linearGradient id="photoTone" x1="0" y1="0" x2="0" y2="1">
          <stop offset="0" stop-color="var(--photo-top)"/>
          <stop offset="1" stop-color="var(--photo-bottom)"/>
        </linearGradient>
      </defs>
      <polygon role="img" aria-label="Photo of a smiling military family in front of their house" points="0,0 322,0 236,125 0,125" fill="url(#photoTone)"/>
      <polygon points="260,0 322,0 302,29" fill="var(--green)"/>
      <polygon points="1002,0 1002,125 906,125" fill="var(--green)"/>
    </svg>
    <svg class="emblem" role="img" aria-label="Emblem of saluting soldiers on a chevron shield under stars" viewBox="0 0 74 106">
      <path d="M10 30 H64 V78 L37 106 L10 78 Z" fill="var(--emblem)"/>
    </svg>
    <div class="offer">
      <div class="offer-line">Ask About Our</div>
      <div class="offer-highlight">"No Credit Score"</div>
      <div class="offer-line">Program for ZMR and QT</div>
    </div>
    <div class="cta">
      <div class="cta-button">Get Started</div>
      <div class="cta-url">www.harborpeakfinancial.com</div>
    </div>
  </div>
</div>
</body>
</html>
```